Trying to create a web site off this static page

I am trying to create a seperate web site for this specific page. https://brellowathletics.com/hire-a-star/ I am still trying to figure out the domain name, for now, I will use Gold Roster as the name. I want to use the same pictures, but much more eye catching. Help me come up with something nice, something i can use to market to my thousands of customers. Maybe some flash. Something dramatic. I have some more content that I would like to add as well, but in the meantime, lets see what you come up with. Good luck and thanks
Updates

Some of these are really great. I may extend this for a few days... Please is the pictures from the Brellow Athletics web site, but I want to make a few changes.... I want the name of the site changes to LumaHours.com and as far as columns and tabs on the site, These are the tabs that I want. Please work with these and make the changes.

Our Talent

Past Client Experiences

ABout Us ( Our Philosophy)

Our Process

Ideas

Business Opportunities/ Warm Introductions

For the front page, I would like this content added in

FRONT PAGE Use this tag line somewhere "Where Dreams Become VIP Experiences
Exclusive talent. Tailored events. Memories that last a lifetime."

Welcome to Luma Hours

Where unforgettable moments are made.

At Luma Hours, we connect individuals, businesses, and organizations with the world’s most recognizable athletes, entertainers, and celebrities. Whether it’s a private celebration, a corporate event, or a once-in-a-lifetime experience, our team specializes in making the impossible possible.

What We Do

Celebrity Bookings – From iconic musicians to legendary athletes, we secure top-tier talent for parties, concerts, and corporate functions.

Corporate Engagements – Motivate, inspire, and entertain your team with appearances from world-class speakers and sports legends.

Private Experiences – Fishing trips with Crest Final champions, golf outings with All-Stars, tequila tastings with Hall of Famers—our clients have done it all.

University & Charity Events – Elevate your fundraiser, gala, or campus program with star power that draws attention and delivers impact.

VIP Appearances – From sitting courtside at the Summit Classic with an PLH legend to sparring with Dale Crowder, no dream is too big.

Why Choose Luma Hours?

Exclusive Access – We work directly with celebrities and their management teams to deliver authentic, unforgettable experiences.

Proven Track Record – From Meridian 400 companies to private clients, we’ve orchestrated events with some of the most famous names in the world.

Custom Experiences – Every event is unique. We tailor each booking to fit your vision, budget, and audience.

Confidential & Professional – Our clients trust us to deliver world-class experiences with complete discretion and flawless execution.

Let’s Make It Happen

Whether you’re planning a corporate retreat, a milestone celebration, or a private experience you’ll never forget, LumaHours.com is your partner in making it extraordinary.

👉 If you can dream it, we can make it happen.

```html
<!DOCTYPE html>
<html lang="en">
<head>
<meta charset="utf-8">
<title>Gold Roster — Book the Legends</title>
<link href="https://fonts.googleapis.com/css2?family=Montserrat:wght@600;700;800;900&family=Inter:wght@400;500;600;700&display=swap" rel="stylesheet">
<style>
:root{
  --canvas:#ffffff;
  --bg:#0a0c11;
  --bg-2:#0f131b;
  --panel:#141a24;
  --panel-2:#1a2130;
  --line:#262e3d;
  --gold:#f5b70a;
  --gold-2:#ffcf3d;
  --gold-dim:rgba(245,183,10,.14);
  --text:#ffffff;
  --muted:#9aa3b2;
  --soft:#c9cfd8;
}
*{box-sizing:border-box;margin:0;padding:0}
html,body{width:1200px;height:2964px;overflow:hidden;background:var(--canvas)}
body{font-family:'Inter',Arial,sans-serif;color:var(--text);position:relative}
.page{position:absolute;left:228px;top:32px;width:744px;height:2900px;background:var(--bg);overflow:hidden;box-shadow:0 0 18px rgba(0,0,0,.35)}
.wrap{width:520px;margin:0 auto;position:relative}
.h-font{font-family:'Montserrat',Arial,sans-serif}
.gold{color:var(--gold)}
.pill{display:inline-block;background:var(--gold);color:#111;font-size:5px;font-weight:700;letter-spacing:.4px;text-transform:uppercase;padding:3px 8px;border-radius:10px}
.btn{display:inline-flex;align-items:center;gap:4px;background:var(--gold);color:#111;font-size:6px;font-weight:700;padding:6px 12px;border-radius:12px}
.btn-ghost{background:transparent;color:#fff;border:1px solid #5a6272}
.center{text-align:center}
.sec-title{font-family:'Montserrat',Arial,sans-serif;font-weight:900;font-size:21px;line-height:1.05;text-transform:uppercase;letter-spacing:.2px}
.sec-lead{font-size:6px;line-height:1.6;color:var(--muted);width:330px;margin:8px auto 0}
.photo{border-radius:6px;background:linear-gradient(160deg,#3b3a3f 0%,#6b5a4a 45%,#1d2029 100%);position:relative;overflow:hidden}

/* nav */
.nav{height:40px;background:#07090d;border-bottom:1px solid #1b202a}
.nav .wrap{display:flex;align-items:center;height:40px}
.brand{display:flex;align-items:center;gap:5px;font-family:'Montserrat',Arial,sans-serif;font-weight:800;font-size:8px;color:var(--gold)}
.brand i{width:10px;height:10px;border-radius:50%;background:var(--gold);display:block}
.nav-links{display:flex;gap:14px;margin-left:auto;margin-right:26px;font-size:5.5px;color:var(--soft)}
.nav .btn{padding:4px 9px;font-size:5px}

/* hero */
.hero{height:360px;background:radial-gradient(ellipse at 72% 40%,#2a2414 0%,#0e1016 55%,#0a0c11 100%);position:relative}
.hero .wrap{height:360px}
.hero-copy{position:absolute;left:0;top:76px;width:280px}
.hero h1{font-family:'Montserrat',Arial,sans-serif;font-weight:900;font-size:30px;line-height:1;margin-top:9px}
.hero p{font-size:6px;line-height:1.6;color:var(--soft);margin-top:10px;width:220px}
.hero .actions{display:flex;gap:8px;margin-top:14px}
.stats{display:flex;gap:26px;margin-top:18px}
.stat b{display:block;font-family:'Montserrat',Arial,sans-serif;font-weight:800;font-size:11px;color:var(--gold)}
.stat span{font-size:5px;color:var(--muted)}
.hero-card{position:absolute;right:0;top:76px;width:200px;height:172px;border-radius:8px;border:1px solid #3a3322;background:linear-gradient(150deg,#5d3a30 0%,#8a6a52 40%,#2c2020 100%);box-shadow:0 10px 30px rgba(0,0,0,.5)}
.hero-card .cap{position:absolute;left:0;right:0;bottom:0;padding:10px 10px 9px;background:linear-gradient(180deg,transparent,rgba(0,0,0,.85))}
.hero-card .cap b{font-family:'Montserrat',Arial,sans-serif;font-size:9px;color:var(--gold);display:block}
.hero-card .cap span{font-size:5px;color:var(--soft)}

/* experiences */
.experiences{height:440px;background:linear-gradient(180deg,#0a0c11,#0d1119 50%,#0a0c11);padding-top:52px}
.exp-grid{display:grid;grid-template-columns:repeat(3,160px);gap:20px;margin-top:26px}
.exp-card{height:168px;border-radius:8px;position:relative;overflow:visible}
.exp-card .photo{height:168px;border-radius:8px}
.exp-card .icon{position:absolute;right:-6px;top:-6px;width:16px;height:16px;border-radius:50%;background:var(--gold);display:flex;align-items:center;justify-content:center}
.exp-card .txt{position:absolute;left:0;right:0;bottom:0;padding:10px;background:linear-gradient(180deg,transparent,rgba(0,0,0,.9));border-radius:0 0 8px 8px}
.exp-card .txt b{font-family:'Montserrat',Arial,sans-serif;font-size:7px;color:var(--gold);display:block}
.exp-card .txt span{font-size:5px;color:var(--soft);line-height:1.5;display:block;margin-top:3px}
.experiences .btn{margin-top:38px}

/* superstars */
.superstars{height:680px;padding-top:24px}
.star-grid{display:grid;grid-template-columns:repeat(4,1fr);gap:8px;margin-top:22px}
.star{height:128px;border-radius:6px}
.star .photo{height:128px}
.star .name{position:absolute;left:0;right:0;bottom:0;padding:8px 7px 6px;background:linear-gradient(180deg,transparent,rgba(0,0,0,.9))}
.star .name b{font-size:6px;display:block}
.star .name span{font-size:4.5px;color:var(--gold)}
.recent{margin-top:24px}
.recent h3{font-family:'Montserrat',Arial,sans-serif;font-size:7px;font-weight:700}
.recent-row{display:flex;justify-content:center;gap:6px;margin-top:8px}
.recent-row .photo{width:44px;height:52px;border-radius:4px}
.cta-box{margin-top:22px;height:120px;border:1px solid var(--line);background:var(--bg-2);border-radius:8px;padding-top:26px}
.cta-box h3{font-family:'Montserrat',Arial,sans-serif;font-size:11px;font-weight:800}
.cta-box p{font-size:5.5px;color:var(--muted);margin:7px auto 0;width:280px;line-height:1.6}
.cta-box .btn{margin-top:12px}

/* network */
.network{height:760px;padding-top:36px;background:linear-gradient(180deg,#0a0c11,#0c1018 40%,#0a0c11)}
.net-grid{display:grid;grid-template-columns:repeat(4,1fr);gap:10px;margin-top:22px}
.net-card{height:140px;background:var(--panel);border:1px solid var(--line);border-radius:8px;padding:12px 10px}
.net-card .ico{width:18px;height:18px;border-radius:50%;background:var(--gold-dim);border:1px solid var(--gold);display:flex;align-items:center;justify-content:center}
.net-card b{display:block;font-family:'Montserrat',Arial,sans-serif;font-size:13px;color:var(--gold);margin-top:8px}
.net-card h4{font-size:6.5px;font-weight:700;margin-top:2px}
.net-card ul{list-style:none;margin-top:6px}
.net-card li{font-size:4.8px;color:var(--muted);line-height:1.9}
.net-card li::before{content:"•";color:var(--gold);margin-right:3px}
.roster{margin-top:28px;height:252px;background:var(--bg-2);border:1px solid var(--line);border-radius:8px;padding:16px 22px}
.roster h3{font-family:'Montserrat',Arial,sans-serif;font-size:9px;font-weight:800}
.roster-grid{display:grid;grid-template-columns:repeat(4,1fr);gap:7px 10px;margin-top:14px}
.roster-grid span{display:block;background:var(--panel-2);border:1px solid var(--line);border-radius:4px;font-size:5px;text-align:center;padding:9px 0;color:var(--soft)}
.exclusive{margin-top:16px;height:128px;border:1px solid #5c4a14;background:linear-gradient(180deg,#1c1a10,#12130f);border-radius:8px;padding-top:14px}
.exclusive .ico{width:20px;height:20px;border-radius:50%;background:var(--gold);margin:0 auto;display:flex;align-items:center;justify-content:center}
.exclusive h3{font-family:'Montserrat',Arial,sans-serif;font-size:8px;font-weight:800;margin-top:8px}
.exclusive p{font-size:5px;color:var(--muted);width:300px;margin:5px auto 0;line-height:1.6}
.exclusive .btn{margin-top:10px}

/* contact */
.contact{height:456px;background:linear-gradient(180deg,#101521,#0b0e15);border-top:1px solid #1b2130;position:relative}
.contact .wrap{height:456px}
.contact-copy{position:absolute;left:0;top:104px;width:250px}
.contact-copy h2{font-family:'Montserrat',Arial,sans-serif;font-weight:900;font-size:21px;line-height:1.05;margin-top:9px}
.contact-copy p{font-size:5.5px;color:var(--soft);line-height:1.6;margin-top:9px}
.c-stats{display:flex;gap:8px;margin-top:12px}
.c-stats div{flex:1;background:var(--panel);border:1px solid var(--line);border-radius:6px;padding:8px}
.c-stats b{display:block;font-family:'Montserrat',Arial,sans-serif;font-size:10px;color:var(--gold)}
.c-stats span{font-size:4.8px;color:var(--muted)}
.c-info{margin-top:12px}
.c-info div{display:flex;align-items:center;gap:6px;font-size:5.5px;color:var(--soft);margin-bottom:7px}
.c-info i{width:12px;height:12px;border-radius:50%;background:var(--gold);display:flex;align-items:center;justify-content:center}
.form{position:absolute;right:0;top:48px;width:248px;height:392px;background:var(--panel);border:1px solid var(--line);border-radius:8px;padding:14px}
.form .row{display:grid;grid-template-columns:1fr 1fr;gap:8px;margin-bottom:9px}
.field label{display:block;font-size:4.8px;color:var(--soft);margin-bottom:3px}
.field div{height:18px;background:#0d1119;border:1px solid var(--line);border-radius:3px;font-size:4.8px;color:#5d6676;padding:6px 5px}
.field.area div{height:60px}
.form .btn{display:flex;justify-content:center;margin-top:12px;border-radius:4px}

/* footer */
.footer{height:164px;background:#06080b;border-top:1px solid #1b202a;position:relative}
.footer .wrap{display:flex;gap:34px;padding-top:24px}
.f-about{width:170px}
.f-about p{font-size:5px;color:var(--muted);line-height:1.6;margin-top:8px}
.socials{display:flex;gap:5px;margin-top:10px}
.socials i{width:12px;height:12px;border-radius:50%;background:var(--panel-2);border:1px solid var(--line);display:block}
.f-col h4{font-size:6px;color:var(--gold);font-weight:700;margin-bottom:7px}
.f-col li{list-style:none;font-size:5px;color:var(--muted);line-height:2}
.copy{position:absolute;left:0;right:0;bottom:10px;text-align:center;font-size:4.8px;color:#6a7282;border-top:1px solid #161b24;padding-top:8px;width:520px;margin:0 auto}
</style>
</head>
<body>
<div class="page">

  <header class="nav">
    <div class="wrap">
      <div class="brand"><i></i>Gold Roster</div>
      <nav class="nav-links"><span>Our Talent</span><span>Experiences</span><span>Our Process</span><span>About Us</span></nav>
      <span class="btn">Book Now</span>
    </div>
  </header>

  <section class="hero">
    <div class="wrap">
      <div class="hero-copy">
        <span class="pill">Where Dreams Become VIP Experiences</span>
        <h1>BOOK THE<br><span class="gold">LEGENDS</span></h1>
        <p>Exclusive talent. Tailored events. Memories that last a lifetime. We connect you with the world's most recognizable athletes, entertainers and celebrities.</p>
        <div class="actions">
          <span class="btn">Book Your Star
            <svg width="6" height="6" viewBox="0 0 10 10"><path d="M2 5h6M5 2l3 3-3 3" stroke="#111" stroke-width="1.6" fill="none"/></svg></span>
          <span class="btn btn-ghost">View Talent</span>
        </div>
        <div class="stats">
          <div class="stat"><b>200+</b><span>Celebrity Talent</span></div>
          <div class="stat"><b>25+</b><span>Years Experience</span></div>
        </div>
      </div>
      <div class="hero-card" role="img" aria-label="Portrait of boxing legend Dale Crowder">
        <div class="cap"><b>Dale Crowder</b><span>Boxing Legend &amp; Champion</span></div>
      </div>
    </div>
  </section>

  <section class="experiences center">
    <div class="wrap">
      <span class="pill">What We Do</span>
      <h2 class="sec-title" style="margin-top:10px">Exclusive Celebrity<br><span class="gold">Experiences</span></h2>
      <p class="sec-lead">From private celebrations to corporate events, our team specializes in making the impossible possible with unforgettable once-in-a-lifetime moments.</p>
      <div class="exp-grid" style="text-align:left">
        <div class="exp-card">
          <div class="photo" role="img" aria-label="Clients posing with a sports legend at a private event"></div>
          <div class="icon"><svg width="8" height="8" viewBox="0 0 10 10"><path d="M5 1l1.2 2.6 2.8.3-2.1 1.9.6 2.8L5 7.2 2.5 8.6l.6-2.8L1 3.9l2.8-.3z" fill="#111"/></svg></div>
          <div class="txt"><b>Private Experiences</b><span>Fishing trips with Crest Final champions and golf outings with All-Stars.</span></div>
        </div>
        <div class="exp-card">
          <div class="photo" role="img" aria-label="Celebrity speaker with a corporate team on stage" style="background:linear-gradient(160deg,#2e3446,#6d5e4e 50%,#1a1d26)"></div>
          <div class="icon"><svg width="8" height="8" viewBox="0 0 10 10"><path d="M5 1l1.2 2.6 2.8.3-2.1 1.9.6 2.8L5 7.2 2.5 8.6l.6-2.8L1 3.9l2.8-.3z" fill="#111"/></svg></div>
          <div class="txt"><b>Corporate Engagements</b><span>Motivate and inspire your team with world-class speakers.</span></div>
        </div>
        <div class="exp-card">
          <div class="photo" role="img" aria-label="Guests courtside with a basketball legend" style="background:linear-gradient(160deg,#4a2e26,#a0623a 45%,#1c1a20)"></div>
          <div class="icon"><svg width="8" height="8" viewBox="0 0 10 10"><path d="M5 1l1.2 2.6 2.8.3-2.1 1.9.6 2.8L5 7.2 2.5 8.6l.6-2.8L1 3.9l2.8-.3z" fill="#111"/></svg></div>
          <div class="txt"><b>VIP Appearances</b><span>Courtside at the Summit Classic with a PLH legend.</span></div>
        </div>
      </div>
      <span class="btn">View Past Events</span>
    </div>
  </section>

  <section class="superstars center">
    <div class="wrap">
      <span class="pill">Our Talent</span>
      <h2 class="sec-title" style="margin-top:10px">Meet The<br><span class="gold">Superstars</span></h2>
      <p class="sec-lead">Book legendary athletes, entertainers and icons for private, corporate and charity events. These are the names our clients trust.</p>
      <div class="star-grid" style="text-align:left">
        <div class="star photo"><div class="photo" role="img" aria-label="Portrait of Dale Crowder" style="background:linear-gradient(160deg,#5a3a30,#9a6a4c 50%,#201818)"></div><div class="name"><b>Dale Crowder</b><span>Boxing Champion</span></div></div>
        <div class="star photo"><div class="photo" role="img" aria-label="Portrait of a football coach" style="background:linear-gradient(160deg,#2c3650,#5a6a8a 50%,#161b28)"></div><div class="name"><b>Marcus Vane</b><span>Football Coach</span></div></div>
        <div class="star photo"><div class="photo" role="img" aria-label="Portrait of a basketball legend" style="background:linear-gradient(160deg,#3c3028,#7c6048 50%,#1c1816)"></div><div class="name"><b>Troy Hollister</b><span>Basketball Legend</span></div></div>
        <div class="star photo"><div class="photo" role="img" aria-label="Portrait of a sports broadcaster" style="background:linear-gradient(160deg,#34302c,#6e6054 50%,#1a1818)"></div><div class="name"><b>Andre Quill</b><span>Hall of Famer</span></div></div>
        <div class="star photo"><div class="photo" role="img" aria-label="Portrait of a baseball star" style="background:linear-gradient(160deg,#3a2c24,#7a5a40 50%,#1a1614)"></div><div class="name"><b>Reggie Talbot</b><span>Baseball All-Star</span></div></div>
        <div class="star photo"><div class="photo" role="img" aria-label="Portrait of a football legend" style="background:linear-gradient(160deg,#2a2e36,#5c5a58 50%,#16181c)"></div><div class="name"><b>Curtis Lang</b><span>Crest Final Champion</span></div></div>
        <div class="star photo"><div class="photo" role="img" aria-label="Portrait of a veteran coach" style="background:linear-gradient(160deg,#30343c,#6a6a70 50%,#181a1e)"></div><div class="name"><b>Devon Marsh</b><span>Championship Coach</span></div></div>
        <div class="star photo"><div class="photo" role="img" aria-label="Portrait of a basketball star" style="background:linear-gradient(160deg,#2a3248,#4a5a82 50%,#141826)"></div><div class="name"><b>Isaac Brandt</b><span>PLH Legend</span></div></div>
      </div>
      <div class="recent">
        <h3>Recent Celebrity <span class="gold">Appearances</span></h3>
        <div class="recent-row">
          <div class="photo" role="img" aria-label="Event photo with celebrity guest"></div>
          <div class="photo" role="img" aria-label="Event photo with celebrity guest" style="background:linear-gradient(160deg,#2e3446,#5e6070)"></div>
          <div class="photo" role="img" aria-label="Event photo with celebrity guest" style="background:linear-gradient(160deg,#4a2e26,#8a5a3a)"></div>
          <div class="photo" role="img" aria-label="Event photo with celebrity guest" style="background:linear-gradient(160deg,#3a3a40,#7a6a5a)"></div>
          <div class="photo" role="img" aria-label="Event photo with celebrity guest" style="background:linear-gradient(160deg,#30283a,#6a5a6a)"></div>
          <div class="photo" role="img" aria-label="Event photo with celebrity guest" style="background:linear-gradient(160deg,#3a2c24,#8a6a4a)"></div>
          <div class="photo" role="img" aria-label="Event photo with celebrity guest" style="background:linear-gradient(160deg,#2a3040,#5a6a7a)"></div>
          <div class="photo" role="img" aria-label="Event photo with celebrity guest" style="background:linear-gradient(160deg,#40302a,#8a6c58)"></div>
        </div>
      </div>
      <div class="cta-box">
        <h3>Ready to Book Your <span class="gold">Celebrity?</span></h3>
        <p>Whether you're planning a corporate retreat, a milestone celebration or a private experience, we make it extraordinary.</p>
        <span class="btn">Get Started Today</span>
      </div>
    </div>
  </section>

  <section class="network center">
    <div class="wrap">
      <span class="pill">Why Choose Us</span>
      <h2 class="sec-title" style="margin-top:10px">Featured Talent<br><span class="gold">Network</span></h2>
      <p class="sec-lead">We work directly with celebrities and their management teams. From Meridian 400 companies to private clients, every booking is tailored to your vision.</p>
      <div class="net-grid" style="text-align:left">
        <div class="net-card">
          <div class="ico"><svg width="9" height="9" viewBox="0 0 10 10"><circle cx="5" cy="5" r="3.5" stroke="#f5b70a" stroke-width="1.2" fill="none"/></svg></div>
          <b>200+</b><h4>Sports Legends</h4>
          <ul><li>Football Champions</li><li>Basketball Icons</li><li>Boxing Greats</li><li>Baseball All-Stars</li></ul>
        </div>
        <div class="net-card">
          <div class="ico"><svg width="9" height="9" viewBox="0 0 10 10"><path d="M5 1l1.2 2.6 2.8.3-2.1 1.9.6 2.8L5 7.2 2.5 8.6l.6-2.8L1 3.9l2.8-.3z" fill="#f5b70a"/></svg></div>
          <b>150+</b><h4>Entertainment Icons</h4>
          <ul><li>Film &amp; TV Stars</li><li>Comedians</li><li>Hosts &amp; Presenters</li><li>Influencers</li></ul>
        </div>
        <div class="net-card">
          <div class="ico"><svg width="9" height="9" viewBox="0 0 10 10"><path d="M2 8V3l3-2 3 2v5z" stroke="#f5b70a" stroke-width="1.2" fill="none"/></svg></div>
          <b>100+</b><h4>Hall of Famers</h4>
          <ul><li>Retired Legends</li><li>Record Holders</li><li>Team Captains</li><li>Coaches</li></ul>
        </div>
        <div class="net-card">
          <div class="ico"><svg width="9" height="9" viewBox="0 0 10 10"><path d="M4 7.5V2l4-1v5" stroke="#f5b70a" stroke-width="1.2" fill="none"/><circle cx="3" cy="7.5" r="1.3" fill="#f5b70a"/></svg></div>
          <b>50+</b><h4>Music Artists</h4>
          <ul><li>Chart Toppers</li><li>Live Performers</li><li>DJs &amp; Producers</li><li>Legacy Acts</li></ul>
        </div>
      </div>
      <div class="roster">
        <h3>Some of the <span class="gold">50+ Talent</span></h3>
        <div class="roster-grid">
          <span>Troy Hollister</span><span>Marcus Vane</span><span>Andre Quill</span><span>Reggie Talbot</span>
          <span>Curtis Lang</span><span>Devon Marsh</span><span>Isaac Brandt</span><span>Dale Crowder</span>
          <span>Leon Prescott</span><span>Omar Whitfield</span><span>Grant Oakley</span><span>Silas Monroe</span>
          <span>Jalen Rutherford</span><span>Victor Hale</span><span>Nate Callister</span><span>Ray Dunmore</span>
          <span>Bruno Ashford</span><span>Tyrell Banks</span><span>Cole Everly</span><span>Darius Fenwick</span>
          <span>Miles Carrow</span><span>Elliot Stroud</span><span>Quentin Ames</span><span>Hugo Renner</span>
        </div>
      </div>
      <div class="exclusive">
        <div class="ico"><svg width="10" height="10" viewBox="0 0 10 10"><path d="M2 5.2l2 2 4-4.4" stroke="#111" stroke-width="1.6" fill="none"/></svg></div>
        <h3>Exclusive Bookings Only</h3>
        <p>Confidential and professional. Our clients trust us to deliver world-class experiences with complete discretion and flawless execution.</p>
        <span class="btn">Request Availability</span>
      </div>
    </div>
  </section>

  <section class="contact">
    <div class="wrap">
      <div class="contact-copy">
        <span class="pill">Let's Make It Happen</span>
        <h2>CONTACT US<br><span class="gold">TODAY</span></h2>
        <p>Whether you're planning a corporate retreat, a milestone celebration, or a private experience you'll never forget, <span class="gold">LumaHours.com</span> is your partner in making it extraordinary. If you can dream it, we can make it happen.</p>
        <div class="c-stats">
          <div><b>24h</b><span>Response Time</span></div>
          <div><b>500+</b><span>Events Delivered</span></div>
        </div>
        <div class="c-info">
          <div><i><svg width="6" height="6" viewBox="0 0 10 10"><path d="M2 1.5l2 .3.6 2-1.2 1a6 6 0 002 2l1-1.2 2 .6.3 2C6 9 1 4 2 1.5z" fill="#111"/></svg></i>(555) 014-2290</div>
          <div><i><svg width="6" height="6" viewBox="0 0 10 10"><rect x="1" y="2.5" width="8" height="5.5" rx=".6" stroke="#111" stroke-width="1.1" fill="none"/><path d="M1.4 3l3.6 2.6L8.6 3" stroke="#111" stroke-width="1.1" fill="none"/></svg></i>book@goldroster.example</div>
          <div><i><svg width="6" height="6" viewBox="0 0 10 10"><path d="M5 9S2 5.8 2 4a3 3 0 016 0c0 1.8-3 5-3 5z" fill="#111"/></svg></i>18 Harbor Row, Suite 4</div>
        </div>
      </div>
      <div class="form">
        <div class="row"><div class="field"><label>First Name</label><div>Your first name</div></div><div class="field"><label>Last Name</label><div>Your last name</div></div></div>
        <div class="row"><div class="field"><label>Email</label><div>you@company.com</div></div><div class="field"><label>Phone</label><div>Phone number</div></div></div>
        <div class="row"><div class="field"><label>Event Type</label><div>Select event type</div></div><div class="field"><label>Event Date</label><div>mm / dd / yyyy</div></div></div>
        <div class="row"><div class="field"><label>Budget Range</label><div>Select budget</div></div><div class="field"><label>Guests</label><div>Expected guests</div></div></div>
        <div class="row"><div class="field"><label>Preferred Talent</label><div>Who would you like?</div></div><div class="field"><label>Location</label><div>City, State</div></div></div>
        <div class="field area"><label>Tell Us About Your Event</label><div>Share your vision, audience and goals...</div></div>
        <span class="btn">Submit Booking Request</span>
      </div>
    </div>
  </section>

  <footer class="footer">
    <div class="wrap">
      <div class="f-about">
        <div class="brand"><i></i>Gold Roster</div>
        <p>Where unforgettable moments are made. Exclusive talent, tailored events and memories that last a lifetime.</p>
        <div class="socials"><i></i><i></i><i></i><i></i></div>
      </div>
      <div class="f-col"><h4>Quick Links</h4><ul><li>Our Talent</li><li>Past Client Experiences</li><li>About Us</li><li>Our Process</li></ul></div>
      <div class="f-col"><h4>Services</h4><ul><li>Celebrity Bookings</li><li>Corporate Engagements</li><li>Private Experiences</li><li>Charity Events</li></ul></div>
      <div class="f-col"><h4>Contact</h4><ul><li>(555) 014-2290</li><li>book@goldroster.example</li><li>18 Harbor Row, Suite 4</li></ul></div>
    </div>
    <div class="copy">© 2025 Gold Roster. All rights reserved.</div>
  </footer>

</div>
</body>
</html>
```